Family business needs stationery redesign with new logo

Family owned company, established in 1987 wanting a brand 'refresh'. We are an electrical, refrigeration and construction company based in the Barkly Region Northern Territory, Australia. We have a new logo we would like to use which is uploaded along with our current letterhead and email signature. We are also dropping the word 'contractors' so please do not include this on any designs. Please note also, the 'orange' color used in our logo and designs should be Northern Territory red ochre which is as follows:

RGB (Hex): #C75B12
PantoneĀ® 159 C
CMYK: 1 / 74 / 100 / 7

We are needing our stationery redesigned using our new logo. Please include letterheads, business cards, envelopes, and email signatures.

We currently use our business letterheads for quotations, invoices, letters, HR matters, and internal memos.

We also need a separate simplified letterhead for internal paperwork such as employee leave forms, meeting agendas, and meeting minutes etc.
Updates

Reason: Needing more submissions of full package designs. We are wanting all our stationery, including business cards, letterheads, email signatures, envelopes, etc to be cohesive. We also require ALL the information, as supplied on our template letterhead, to be included on the new letterhead designs. including electrical license no.etc Thank you, R&K

Reason: needing more time as work has got in the way of looking over designs. A lot of designs not meeting the brief/criteria.

Industry/Entity Type

Business

Colors
0355a3
f37122

Requirements
Must have
• The 'orange' color used in the designs should be Northern Territory red ochre which is as follows:
• RGB (Hex): #C75B12
• PantoneĀ® 159 C
• CMYK: 1 / 74 / 100 / 7
• ***MUST INCLUDE ALL INFORMATION THAT IS ON OUR CURRENT LETTERHEAD***
Should not have
• Please do not include the word 'contractors'

```html
<!DOCTYPE html>
<html lang="en">
<head>
<meta charset="utf-8">
<title>R&amp;K Stationery Set</title>
<link href="https://fonts.googleapis.com/css2?family=Source+Sans+3:wght@400;600;700&display=swap" rel="stylesheet">
<style>
:root{
  --navy:#26336b;
  --ochre:#dd5c1b;
  --ink:#5a5a5a;
  --paper:#ffffff;
  --stage:#2e2e2e;
}
*{margin:0;padding:0;box-sizing:border-box}
html,body{width:1200px;height:922px;overflow:hidden}
body{background:var(--stage);font-family:'Source Sans 3',sans-serif;position:relative;color:var(--ink)}
.sheet{position:absolute;background:var(--paper);overflow:hidden;box-shadow:0 2px 6px rgba(0,0,0,.5)}
.wordmark{font-weight:700;color:var(--navy);line-height:1;letter-spacing:.5px;position:absolute;display:flex;align-items:center}
.wordmark.on-dark{color:#fff}
.contact{list-style:none}
.contact li{display:flex;align-items:center;gap:4px;white-space:nowrap}
.contact svg{width:7px;height:7px;fill:var(--ochre);flex:none}
.web{color:var(--ochre)}

/* footer band */
.band{position:absolute;left:0;right:0;bottom:0;height:21px;background:var(--navy);color:#fff;font-size:8.5px;display:flex;align-items:center}
.band .services{padding-left:32px}
.band .services b{color:var(--ochre);font-weight:400}
.band .site{position:absolute;top:0;right:0;bottom:0;background:var(--ochre);clip-path:polygon(8px 0,100% 0,100% 100%,0 100%);display:flex;align-items:center;padding-left:30px}

/* letterhead */
.letterhead{left:21px;top:191px;width:549px;height:710px}
.letterhead .wordmark{left:36px;top:42px;font-size:38px}
.letterhead .address{position:absolute;left:379px;top:35px;font-size:8.5px;line-height:10px}
.letterhead .contact{position:absolute;left:379px;top:70px;font-size:8.5px;line-height:10px}
.letterhead .legal{position:absolute;left:0;right:0;top:671px;text-align:center;font-size:7.5px}
.legal i{color:var(--ochre);font-style:normal;padding:0 3px}
.letterhead .band .site{width:156px}

/* email signature */
.email-signature{left:607px;top:21px;width:359px;height:141px}
.email-signature .wordmark{left:20px;top:20px;font-size:22px}
.email-signature .name{position:absolute;left:16px;top:60px;font-size:11px;font-weight:700;color:var(--navy)}
.email-signature .role{position:absolute;left:16px;top:74px;font-size:6.5px}
.email-signature .contact{position:absolute;left:16px;top:91px;font-size:6.8px;line-height:9px}
.email-signature .divider{position:absolute;left:166px;top:93px;width:1px;height:33px;background:var(--ink)}
.email-signature .postal{position:absolute;left:173px;top:92px;font-size:6.8px;line-height:9px}

/* card front */
.card-front{left:607px;top:190px;width:226px;height:130px;border-radius:6px}
.card-front .wordmark{left:0;right:0;top:15px;justify-content:center;font-size:22px}
.card-front .name{position:absolute;left:0;right:0;top:61px;text-align:center;font-size:8.5px;font-weight:700;color:var(--navy)}
.card-front .role{position:absolute;left:0;right:0;top:72px;text-align:center;font-size:5px}
.card-front .panel{position:absolute;left:0;right:0;top:84px;bottom:0;background:var(--navy);border-top:2px solid var(--ochre);color:#fff;font-size:5.2px;line-height:7.3px;font-weight:600}
.card-front .contact{position:absolute;left:11px;top:6px}
.card-front .contact svg{width:5px;height:5px}
.card-front .postal{position:absolute;right:12px;top:6px;text-align:right}

/* card back */
.card-back{left:847px;top:190px;width:226px;height:130px;border-radius:6px;background:var(--navy)}
.card-back .wordmark{left:0;right:0;top:48px;justify-content:center;font-size:34px}
.card-back .tagline{position:absolute;left:0;right:0;top:112px;text-align:center;color:#fff;font-size:6px;font-weight:600}
.card-back .tagline b{color:var(--ochre);font-weight:400}

/* envelopes */
.envelope-flap{left:607px;top:366px;width:574px;height:250px;background:transparent;box-shadow:none}
.envelope-flap .body{position:absolute;left:0;top:0;width:100%;height:100%;background:var(--paper);box-shadow:0 2px 6px rgba(0,0,0,.5)}
.envelope-flap svg.flap{position:absolute;left:0;top:0}
.envelope-flap .wordmark{left:0;right:0;top:26px;justify-content:center;font-size:22px}
.envelope-dl{left:607px;top:651px;width:574px;height:251px}
.envelope-dl .wordmark{left:30px;top:32px;font-size:34px}
.envelope-dl .address{position:absolute;left:25px;top:80px;font-size:8.5px;line-height:10.5px}
.envelope-dl .band .site{width:147px}
</style>
</head>
<body>
<svg width="0" height="0" style="position:absolute">
  <symbol id="i-phone" viewBox="0 0 10 10"><path d="M2 0h2l1 3-1.5 1a6 6 0 0 0 2.5 2.5L7 5l3 1v2a2 2 0 0 1-2 2A8 8 0 0 1 0 2a2 2 0 0 1 2-2z"/></symbol>
  <symbol id="i-mobile" viewBox="0 0 10 10"><path d="M3 0h4a1 1 0 0 1 1 1v8a1 1 0 0 1-1 1H3a1 1 0 0 1-1-1V1a1 1 0 0 1 1-1zm0 1.5v6h4v-6z"/></symbol>
  <symbol id="i-fax" viewBox="0 0 10 10"><path d="M2.5 0h5v3h-5zM0 3.5h10V8H8v2H2V8H0zM3 6.5v2.5h4V6.5z"/></symbol>
  <symbol id="i-mail" viewBox="0 0 10 10"><path d="M0 2h10v6H0zm1 1 4 3 4-3z"/></symbol>
</svg>

<!-- Letterhead -->
<section class="sheet letterhead">
  <div class="wordmark">R&amp;K</div>
  <p class="address">PO Box 4410, 52 Ridgeway St<br>Dustvale NT 0870</p>
  <ul class="contact">
    <li><svg><use href="#i-phone"/></svg>08 8900 1234</li>
    <li><svg><use href="#i-fax"/></svg>08 8900 5678</li>
    <li><svg><use href="#i-mail"/></svg>danawhitford@rkgroup.com.au</li>
  </ul>
  <p class="legal">ABN 00 123 456 789<i>|</i>Refrigerant Trading Authorisation AU00000<i>|</i>NT Electrical Contractors License 09999</p>
  <div class="band">
    <span class="services">Electrical <b>•</b> Refrigeration <b>•</b> Building Services</span>
    <span class="site">www.rkgroup.com.au</span>
  </div>
</section>

<!-- Email signature -->
<section class="sheet email-signature">
  <div class="wordmark">R&amp;K</div>
  <h2 class="name">Dana Whitford</h2>
  <p class="role">Corporate Services Manager, R&amp;K</p>
  <ul class="contact">
    <li><svg><use href="#i-phone"/></svg>08 8900 1234</li>
    <li><svg><use href="#i-mobile"/></svg>0400 111 222</li>
    <li><svg><use href="#i-fax"/></svg>08 8900 5678</li>
    <li><svg><use href="#i-mail"/></svg>danawhitford@rkgroup.com.au</li>
  </ul>
  <span class="divider"></span>
  <p class="postal">PO Box 4410<br>52 Ridgeway St<br>Dustvale NT 0870<br><span class="web">www.rkgroup.com.au</span></p>
</section>

<!-- Business card front -->
<section class="sheet card-front">
  <div class="wordmark">R&amp;K</div>
  <h2 class="name">Dana Whitford</h2>
  <p class="role">Corporate Services Manager, R&amp;K</p>
  <div class="panel">
    <ul class="contact">
      <li><svg><use href="#i-phone"/></svg>08 8900 1234</li>
      <li><svg><use href="#i-mobile"/></svg>0400 111 222</li>
      <li><svg><use href="#i-fax"/></svg>08 8900 5678</li>
      <li><svg><use href="#i-mail"/></svg>danawhitford@rkgroup.com.au</li>
    </ul>
    <p class="postal">PO Box 4410<br>52 Ridgeway St<br>Dustvale NT 0870<br><span class="web">www.rkgroup.com.au</span></p>
  </div>
</section>

<!-- Business card back -->
<section class="sheet card-back">
  <div class="wordmark on-dark">R&amp;K</div>
  <p class="tagline">Electrical <b>•</b> Refrigeration <b>•</b> Building Services</p>
</section>

<!-- Envelope with flap -->
<section class="sheet envelope-flap">
  <div class="body"></div>
  <svg class="flap" width="574" height="76" viewBox="0 0 574 76">
    <path d="M0 0H574L566 58Q563 73 548 73H26Q11 73 8 58Z" fill="#26336b"/>
  </svg>
  <div class="wordmark on-dark">R&amp;K</div>
</section>

<!-- DL envelope -->
<section class="sheet envelope-dl">
  <div class="wordmark">R&amp;K</div>
  <p class="address">PO Box 4410, 52 Ridgeway St<br>Dustvale NT 0870</p>
  <div class="band">
    <span class="services">Electrical <b>•</b> Refrigeration <b>•</b> Building Services</span>
    <span class="site">www.rkgroup.com.au</span>
  </div>
</section>
</body>
</html>
```